Webdesign for blog, vlog and website
The designs for my website were better than what I expected when I started this contest. I knew I needed a call-to-action on my homepage, but I thought it wouldn't be possible and I didn't ask for it either. But Anselmo did it anyway. Furthermore, his design looked very good. For that reason I selected him as winner already before I should. I am very happy.

```html
<!DOCTYPE html>
<html lang="en">
<head>
<meta charset="utf-8">
<title>Tavilon – Believes and Convictions</title>
<link rel="stylesheet" href="https://fonts.googleapis.com/css2?family=Montserrat:wght@300;400;600;700&family=Open+Sans:wght@400;600;700&display=swap">
<style>
  :root {
    --brand: #1b1bd6;
    --hero: #5a5cbc;
    --badge: #1414f0;
    --video-bg: #1aa6e6;
    --ink: #333340;
    --muted: #8a8a96;
    --rule: #e4e4ec;
    --white: #ffffff;
    --page: #ffffff;
  }
  * { box-sizing: border-box; margin: 0; padding: 0; }
  html, body { width: 1200px; height: 800px; overflow: hidden; background: var(--page); }
  body { font-family: "Open Sans", Arial, sans-serif; color: var(--ink); }

  .site { width: 1200px; height: 800px; display: flex; flex-direction: column; overflow: hidden; }

  /* Header */
  .site-header { height: 63px; display: flex; align-items: center; border-bottom: 1px solid var(--rule); padding: 0 0 0 250px; }
  .brand { display: flex; align-items: center; gap: 7px; color: var(--brand); font-family: "Open Sans", sans-serif; font-weight: 700; font-size: 20px; }
  .brand-dot { width: 14px; height: 14px; border-radius: 50%; background: var(--brand); }
  .main-nav { margin-left: 185px; display: flex; align-items: center; gap: 10px; font-size: 9.5px; font-weight: 600; letter-spacing: .3px; color: var(--ink); }
  .main-nav a { color: inherit; text-decoration: none; }
  .main-nav a.active { color: var(--brand); border-bottom: 2px solid var(--brand); padding-bottom: 2px; }
  .main-nav .sep { width: 3px; height: 3px; border-radius: 50%; background: var(--muted); }
  .cart-dot { width: 11px; height: 11px; border-radius: 50%; background: #d8343a; }

  /* Hero */
  .hero { height: 278px; background: var(--hero); display: flex; flex-direction: column; align-items: center; padding-top: 78px; color: var(--white); }
  .hero h1 { font-family: "Montserrat", sans-serif; font-weight: 400; font-size: 33px; letter-spacing: -.3px; }
  .hero .tagline { font-family: "Montserrat", sans-serif; font-size: 13px; letter-spacing: 3px; margin-top: 4px; }
  .search { margin-top: 24px; display: flex; gap: 6px; }
  .search-input { width: 220px; height: 27px; background: var(--white); border-radius: 2px; font-size: 8px; color: #aaa; padding: 8px 10px; }
  .search-btn { width: 117px; height: 27px; background: var(--hero); border: 1px solid var(--white); border-radius: 2px; font-size: 11px; display: flex; align-items: center; justify-content: center; }

  /* Filters */
  .filters { height: 38px; display: flex; align-items: center; font-size: 7.5px; font-weight: 600; letter-spacing: .2px; color: var(--ink); }
  .filter-group { display: flex; align-items: center; gap: 9px; }
  .filter-group.topics { margin-left: 246px; }
  .filter-group.formats { margin-left: 108px; }
  .filter-group .on { color: var(--brand); }
  .filter-group .sep { width: 3px; height: 3px; border-radius: 50%; background: var(--muted); }

  /* Feed */
  .feed { flex: 1; display: grid; grid-template-columns: 397px 200px 205px 202px 196px; grid-template-rows: 209px 1fr; overflow: hidden; }
  .video-tile { grid-row: 1 / 3; background: var(--video-bg); position: relative; }
  .play { position: absolute; left: 148px; top: 168px; }
  .media { background: linear-gradient(160deg, #3d4a7a, #9aa3bd); position: relative; }
  .media.sport { background: linear-gradient(160deg, #4b5a86, #a85a48); }
  .media.portrait { background: linear-gradient(180deg, #b9d6ea, #e9e3dc); }
  .date-badge { position: absolute; left: 0; top: 64px; width: 34px; height: 40px; background: var(--badge); color: var(--white); text-align: center; }
  .date-badge .month { display: block; font-size: 5px; margin-top: 4px; letter-spacing: .2px; }
  .date-badge .day { display: block; font-family: "Montserrat", sans-serif; font-size: 19px; line-height: 22px; }

  .post { padding: 26px 16px 0 16px; }
  .post h2 { font-size: 7px; font-weight: 700; color: var(--brand); line-height: 1.35; text-transform: uppercase; }
  .post p { font-size: 6px; line-height: 1.55; color: var(--muted); margin-top: 9px; }
  .read-more { display: flex; align-items: center; gap: 4px; margin-top: 9px; font-size: 6px; font-weight: 700; color: var(--brand); }
  .read-more svg { display: block; }
  .post.wide { grid-column: 2 / 4; padding-top: 14px; }
  .post.row2 { padding-top: 14px; }
</style>
</head>
<body>
<div class="site">
  <header class="site-header">
    <div class="brand"><span class="brand-dot"></span>Tavilon</div>
    <nav class="main-nav">
      <a class="active" href="#">HOME</a><span class="sep"></span>
      <a href="#">BLOG</a><span class="sep"></span>
      <a href="#">VLOG</a><span class="sep"></span>
      <a href="#">FORUM</a><span class="sep"></span>
      <a href="#">ABOUT ME</a><span class="sep"></span>
      <a href="#">CONTACT</a><span class="sep"></span>
      <a href="#">SHOP</a><span class="cart-dot"></span>
    </nav>
  </header>

  <section class="hero">
    <h1>Believes and Convictions</h1>
    <p class="tagline">WHAT'S YOUR IDEAS?</p>
    <div class="search">
      <div class="search-input">Search ideas or blog</div>
      <div class="search-btn">Search</div>
    </div>
  </section>

  <nav class="filters">
    <div class="filter-group topics">
      <span class="on">ALL IDEAS</span><span class="sep"></span>
      <span>POLITICS</span><span class="sep"></span>
      <span>HEALTH</span><span class="sep"></span>
      <span>FOOD &amp; RECIPE</span><span class="sep"></span>
      <span>SPORTS</span><span class="sep"></span>
      <span>RANDOM</span>
    </div>
    <div class="filter-group formats">
      <span class="on">BLOG &amp; VLOGS</span><span class="sep"></span>
      <span>ONLY VLOGS</span><span class="sep"></span>
      <span>ONLY BLOG</span>
    </div>
  </nav>

  <main class="feed">
    <div class="video-tile" role="img" aria-label="Vlog still of a smiling woman in front of a blue backdrop">
      <svg class="play" width="48" height="48" viewBox="0 0 48 48" aria-hidden="true">
        <circle cx="24" cy="24" r="21" fill="none" stroke="#fff" stroke-width="2.5"/>
        <path d="M19 14 L34 24 L19 34 Z" fill="none" stroke="#fff" stroke-width="2.5" stroke-linejoin="round"/>
      </svg>
    </div>

    <article class="post">
      <h2>Lorem ipsum dolor sit amet, consectetur adipiscing elit</h2>
      <p>Lorem ipsum dolor sit amet, consectetur adipiscing elit, sed do eiusmod tempor incididunt ut labore et dolore magna aliqua.</p>
      <p>Lorem ipsum dolor sit amet, consectetur adipiscing elit, sed do eiusmod tempor incididunt ut labore et dolore magna.</p>
      <div class="read-more"><svg width="8" height="8" viewBox="0 0 8 8"><circle cx="4" cy="4" r="3.4" fill="none" stroke="currentColor" stroke-width=".8"/><path d="M3 2.4 L4.6 4 L3 5.6" fill="none" stroke="currentColor" stroke-width=".8"/></svg>READ MORE</div>
    </article>

    <div class="media" role="img" aria-label="Press photo of a politician in a dark suit and red tie">
      <div class="date-badge"><span class="month">FEBRUARY</span><span class="day">20</span></div>
    </div>

    <article class="post">
      <h2>Lorem ipsum dolor sit amet, consectetur adipiscing elit</h2>
      <p>Lorem ipsum dolor sit amet, consectetur adipiscing elit, sed do eiusmod tempor incididunt ut labore et dolore magna aliqua.</p>
      <p>Lorem ipsum dolor sit amet, consectetur adipiscing elit, sed do eiusmod tempor incididunt ut labore et dolore magna.</p>
      <div class="read-more"><svg width="8" height="8" viewBox="0 0 8 8"><circle cx="4" cy="4" r="3.4" fill="none" stroke="currentColor" stroke-width=".8"/><path d="M3 2.4 L4.6 4 L3 5.6" fill="none" stroke="currentColor" stroke-width=".8"/></svg>READ MORE</div>
    </article>

    <div class="media sport" role="img" aria-label="Marathon runners racing along a city street">
      <div class="date-badge"><span class="month">MARCH</span><span class="day">18</span></div>
    </div>

    <article class="post wide">
      <h2>Lorem ipsum dolor sit amet, consectetur adipiscing elit lorem ipsum dolor sit amet, consectetur adipiscing elit</h2>
      <p>Lorem ipsum dolor sit amet, consectetur adipiscing elit, sed do eiusmod tempor incididunt ut labore et dolore magna aliqua.</p>
    </article>

    <div class="media portrait" role="img" aria-label="Portrait of a person against a light sky"></div>

    <article class="post row2">
      <h2>Lorem ipsum dolor sit amet, consectetur adipiscing elit</h2>
      <p>Lorem ipsum dolor sit amet, consectetur adipiscing elit, sed do eiusmod tempor incididunt ut labore et dolore magna aliqua.</p>
    </article>
  </main>
</div>
</body>
</html>
```